Music Festival in Colorado Needs Awesome Flier Design

We need an eye-catching & captivating flier design for an annual music festival in Denver, CO (USA). The festival features the best Colorado musicians within the genres of jam - funk - bluegrass - electronic - reggae - rock.

The design should look clean and professional while still being creative and unique. The past three years' flier designs are attached, as well as the logo and some other designs that match the aesthetic of what we're looking for.

This festival has a big element of Colorado pride so any

Target Market(s)

Hippies - live music enthusiasts - partiers. Ages 21 - 40.

Industry/Entity Type

Entertainment

Colors
0355a3
ec1f27
ffffff
fbed22

Requirements
Must have
• Attached design text.
Nice to have
• - Quality texture and psychedelic elements.
• - Colorado pride elements; color scheme (red, white, blue & yellow), flag, ect.
• - Nature elements are awesome but this is also a downtown festival so keep that in mind.
Should not have
• Cheesy artwork.

```html
<!DOCTYPE html>
<html lang="en">
<head>
<meta charset="utf-8">
<title>Pass the Sound 2018</title>
<link href="https://fonts.googleapis.com/css2?family=Oswald:wght@700&family=Jost:ital,wght@0,700;1,700&display=swap" rel="stylesheet">
<style>
  :root {
    --blue: #0355a3;
    --blue-deep: #0a4fa0;
    --sky: #3f8fd0;
    --green: #4fae3c;
    --yellow: #fbed22;
    --red: #ec1f27;
    --red-dark: #c8141c;
    --white: #ffffff;
  }
  * { margin: 0; padding: 0; box-sizing: border-box; }
  html, body { width: 785px; height: 1200px; overflow: hidden; }
  body { background: var(--white); }

  .flier {
    position: relative;
    width: 785px;
    height: 1200px;
    overflow: hidden;
    background: linear-gradient(180deg,
      var(--blue) 0%,
      var(--blue-deep) 50%,
      var(--sky) 60%,
      var(--green) 73%,
      var(--yellow) 81%,
      var(--yellow) 100%);
    text-align: center;
  }

  .brand {
    position: absolute;
    top: 108px;
    left: 0;
    width: 100%;
    font-family: "Jost", sans-serif;
    font-weight: 700;
    font-size: 66px;
    line-height: 1;
    color: var(--yellow);
    text-transform: uppercase;
  }

  .dates {
    position: absolute;
    top: 270px;
    left: 0;
    width: 100%;
    font-family: "Oswald", sans-serif;
    font-weight: 700;
    font-size: 40px;
    line-height: 50px;
    color: var(--yellow);
  }

  .lineup {
    position: absolute;
    top: 328px;
    left: 0;
    width: 100%;
    font-family: "Jost", sans-serif;
    font-weight: 700;
    color: var(--white);
    text-transform: uppercase;
  }
  .lineup p { white-space: nowrap; }
  .headliner { font-size: 40px; line-height: 54px; }
  .tier-two { font-size: 30px; line-height: 35px; }
  .tier-two.lead { margin-top: 2px; }
  .tier-three { font-size: 19.5px; line-height: 26.4px; }
  .tier-three.lead { margin-top: 4px; }
  .tier-three.dark { color: var(--blue); }

  .venue {
    position: absolute;
    top: 862px;
    left: 0;
    width: 100%;
    font-family: "Jost", sans-serif;
    font-weight: 700;
    font-style: italic;
    font-size: 21px;
    line-height: 28px;
    color: var(--red);
    text-transform: uppercase;
  }

  .mountains {
    position: absolute;
    left: 0;
    bottom: 0;
    width: 100%;
    height: 236px;
    background: linear-gradient(180deg, var(--red) 0%, #ef6a6e 45%, var(--red-dark) 100%);
  }

  .tickets {
    position: absolute;
    left: 0;
    bottom: 10px;
    width: 100%;
    font-family: "Oswald", sans-serif;
    font-weight: 700;
    font-size: 27px;
    line-height: 34px;
    color: var(--yellow);
  }
</style>
</head>
<body>
  <main class="flier">
    <header class="brand">Pass the Sound</header>

    <h1 class="dates">MAY 11TH - 13TH, 2018 (6TH ANNUAL)</h1>

    <section class="lineup">
      <p class="headliner">MARLOW FINCH BAND •</p>
      <p class="headliner">HOLLOW PINES ORCHESTRA •</p>
      <p class="tier-two lead">LOOP THEORY • THE LANTERN KIDS •</p>
      <p class="tier-two">RUE CASTILLO &amp; CO • NIGHTJAR ORCHES-</p>
      <p class="tier-two">TRA • QUILLWORT • BRAMBLECORE • PORCH-</p>
      <p class="tier-two">LIGHT RAMBLE • JUNIPER ENSEMBLE •</p>
      <p class="tier-two">TIN CANYON • THE LOW MESA • VELVETFOLD</p>
      <p class="tier-three lead">• TAMSEN • OAKHOLLOW • SABLEWIND • CEDAR JUNCTION •</p>
      <p class="tier-three">BRIGHTWATER • HUSHMOTH • PAPER COMET • CEDAR JUNCTION •</p>
      <p class="tier-three">RIDGELINE • THE HONEY WRENS • DUSK PARADE • WREN HALVORSEN</p>
      <p class="tier-three">BAND • BRASSWORK • IRIE CANYON • GLOWFERN • SALTGRASS</p>
      <p class="tier-three">• THE LOAFERS • AUNT CLOVER •</p>
      <p class="tier-three">TIMBERLINE COLLECTIVE • SOLVISTA • KETTLE DRUM •</p>
      <p class="tier-three">GROOVE CANYON •</p>
      <p class="tier-three dark">LAZY ADMIRAL • DJ HALCYON • MOONRAKE •</p>
      <p class="tier-three dark">SIGNAL NINE • SUMMIT HUM • FRACTALYN •</p>
    </section>

    <address class="venue">
      PINE STREET YARD<br>
      418 W. 42ND AVE<br>
      DENVER, CO 80211
    </address>

    <div class="mountains" role="img" aria-label="Red rocky mountain range with white snow patches along the bottom of the poster"></div>

    <footer class="tickets">TICKETS &amp; MORE INFO @ WWW.PASSTHESOUNDFEST.COM</footer>
  </main>
</body>
</html>
```